Lower Cost Storage Scheme Email marketing campaign for Corvel Energy

Design a visually engaging and professional marketing email to promote the upcoming Federal Government Battery Subsidy to our existing solar clients, encouraging them to install a battery system now to maximise savings. email content example "Subject: ⚡ Federal Government Battery Subsidy is Coming – Maximise Your Solar Savings

Body:
Hi [First Name],

Great news! With the federal election now decided, the Federal Government’s Home Battery Subsidy Program is officially on the way.

While the scheme hasn’t formally launched yet, it's guaranteed—and like the solar rebate before it, the subsidy reduces each year, so the earlier you install, the more you’ll save.

Crucially, the subsidy is only available once per household, so it makes sense to install a system that fully meets your home's battery needs right from the start.

Why add a battery to your existing solar system now?
✅ Store your excess solar energy instead of sending it back to the grid for low feed-in tariffs
✅ Use your stored solar power at night, when electricity prices are highest (typically 5–8pm)
✅ Slash your power bills and avoid rising time-of-use charges
✅ Protect your home from power outages
✅ Increase your self-sufficiency and long-term energy security

If you’ve already installed solar with us, now is the ideal time to complete your setup with a battery system designed to maximise your return—and take full advantage of this one-off federal subsidy.

Call us today or reply to this email to secure your spot and beat the rush.

Let your solar work smarter for your home,
The Corvel Energy Team"

Target Market(s)

Content: We’ve provided the copy (see attached or below). The key points to emphasise in the design are: The urgency (subsidy winds down each year, limited to one per household). The benefits of installing a battery now, including energy savings, time-of-use charge avoidance, and self-sufficiency. Call to action: “Call us today or reply to this email to secure your spot and beat the rush.”

Industry/Entity Type

Renewable Energy

Colors
0054AA
0677BA
7BADD7
CADEEF
E8F1F8
EB3D1F
EC4F4E
F09395
F8D3D4
FCEDEE

Requirements
Must have
• Clean, modern, and trustworthy – aligned with Corvel Energy branding. Bold headers and icons to make key points stand out. Include visual elements such as: A solar battery image Infographic or icon-style section showing key battery benefits (e.g. bill savings, backup power, self-consumption) Highlighted call-to-action button (“Secure My Battery Now” or “Beat the Rush”)
Nice to have
• I would like to have our company imagery (Corvel Energy) alongside the battery brands we offer being Velto, QMP, Brimlite and TervoPWR
Should not have
• Unsure

```html
<!DOCTYPE html>
<html lang="en">
<head>
<meta charset="utf-8">
<title>Corvel Energy – Battery Subsidy Email</title>
<link href="https://fonts.googleapis.com/css2?family=DM+Sans:wght@400;500;700&family=Oswald:wght@400;500&display=swap" rel="stylesheet">
<style>
:root{
  --red:#c21f2d;
  --red-dark:#a81a27;
  --navy:#2b3345;
  --navy-panel:rgba(43,51,69,.94);
  --ink:#2a2f3a;
  --muted:#4a505c;
  --paper:#ffffff;
  --mist:#e9ecf1;
  --velto:#1a8fd8;
  --qmp:#e0202a;
  --brimlite:#f07a12;
  --tervo:#333a44;
}
*{margin:0;padding:0;box-sizing:border-box}
html,body{width:1200px;height:4000px;overflow:hidden;background:var(--paper)}
body{font-family:'DM Sans',sans-serif;color:var(--ink);position:relative}
.email{position:relative;width:1200px;height:4000px;background:var(--paper);overflow:hidden}

.hero{position:absolute;left:0;top:0;width:1200px;height:1200px}
.hero svg{position:absolute;left:0;top:0}
.brand{position:absolute;left:0;top:100px;width:1200px;text-align:center}
.brand-name{display:inline-flex;align-items:center;gap:22px;font-family:'DM Sans',sans-serif;font-weight:700;font-size:82px;letter-spacing:2px;color:var(--red-dark);line-height:1}
.brand-mark{width:64px;height:64px;background:var(--red-dark)}
.brand-tag{margin-top:36px;font-size:27px;color:var(--ink);letter-spacing:.5px}
.hero-title{position:absolute;left:126px;top:548px;width:640px;font-weight:500;font-size:56px;line-height:66px;color:#fff}

.headline{position:absolute;left:52px;top:1100px;padding-left:52px;border-left:10px solid var(--red);font-family:'Oswald',sans-serif;font-weight:400;font-size:98px;line-height:96px;color:var(--navy);letter-spacing:1px}

.intro{position:absolute;left:102px;top:1364px;width:1000px}
.greet{font-weight:700;font-size:34px;margin-bottom:46px}
.lead{font-weight:500;font-size:38px;line-height:54px;margin-bottom:40px;color:var(--ink)}
.body-copy{font-size:30px;line-height:44px;color:var(--muted);margin-bottom:40px}
.hl{color:var(--red);font-weight:500}

.benefits{position:absolute;left:0;top:2036px;width:1200px;height:786px}
.benefits-bg{position:absolute;inset:0;background:linear-gradient(120deg,#4b5260,#262b34 45%,#3d434e)}
.benefits-panel{position:absolute;left:80px;top:0;width:1040px;height:786px;background:var(--navy-panel)}
.benefits-head{position:absolute;left:0;top:36px;width:1040px;height:110px;background:var(--red);color:#fff;font-family:'Oswald',sans-serif;font-size:42px;display:flex;align-items:center;justify-content:center;letter-spacing:.5px}
.benefit-list{position:absolute;left:70px;top:190px;list-style:none}
.benefit{display:flex;align-items:flex-start;height:120px}
.benefit svg{width:50px;height:54px;margin:6px 62px 0 0;flex:none}
.benefit p{font-size:30px;line-height:40px;color:#e8ebf0;width:800px}
.benefit b{color:#fff;font-weight:700}

.outro{position:absolute;left:70px;top:2884px;width:1060px;text-align:center;font-size:30px;line-height:43px;color:var(--muted)}
.cta-arrow{position:absolute;left:582px;top:3072px}
.cta{position:absolute;left:460px;top:3114px;width:280px;height:66px;border-radius:8px;background:var(--red);color:#fff;font-weight:500;font-size:38px;display:flex;align-items:center;justify-content:center}
.cta-sub{position:absolute;left:0;top:3200px;width:1200px;text-align:center;font-weight:700;font-size:30px;color:var(--ink)}
.cta-sub .hl{font-weight:700}
.signoff{position:absolute;left:0;top:3306px;width:1200px;text-align:center;font-size:30px;color:var(--muted)}
.team{position:absolute;left:0;top:3366px;width:1200px;display:flex;justify-content:center;align-items:center;gap:16px;font-family:'Oswald',sans-serif;font-size:46px;color:var(--navy)}
.team-mark{width:34px;height:34px;border:5px solid var(--red)}

.partners{position:absolute;left:96px;top:3500px;width:1008px;height:126px;border-top:2px solid #d8dbe0;border-bottom:2px solid #d8dbe0;display:flex;align-items:center;justify-content:space-between;padding:0 4px}
.partner{font-weight:700;font-size:46px;letter-spacing:1px}
.p-velto{color:var(--velto)}
.p-qmp{color:var(--qmp)}
.p-brimlite{color:var(--brimlite)}
.p-tervo{color:var(--tervo);font-weight:500;font-size:42px}

.footer{position:absolute;left:0;top:3640px;width:1200px;height:360px}
.footer svg{position:absolute;left:0;top:0}
.phone-badge{position:absolute;left:554px;top:44px;width:92px;height:92px;border-radius:50%;background:var(--navy);display:flex;align-items:center;justify-content:center}
.phone{position:absolute;left:0;top:164px;width:1200px;text-align:center;font-family:'Oswald',sans-serif;font-size:72px;color:var(--navy);letter-spacing:1px}
.web{position:absolute;left:0;top:266px;width:1200px;text-align:center;font-weight:500;font-size:30px;color:var(--ink)}
</style>
</head>
<body>
<div class="email">

  <section class="hero">
    <svg width="1200" height="1200" viewBox="0 0 1200 1200">
      <defs>
        <linearGradient id="sky" x1="0" y1="0" x2="0" y2="1">
          <stop offset="0" stop-color="#f3f4f6"/>
          <stop offset="0.3" stop-color="#dfe2e7"/>
          <stop offset="0.55" stop-color="#5a6270"/>
          <stop offset="1" stop-color="#2a2e36"/>
        </linearGradient>
        <linearGradient id="unit" x1="0" y1="0" x2="1" y2="0">
          <stop offset="0" stop-color="#d9dde3"/>
          <stop offset="1" stop-color="#f7f8fa"/>
        </linearGradient>
      </defs>
      <rect x="0" y="0" width="1200" height="1100" fill="url(#sky)" role="img" aria-label="Photo of a modern house roof fitted with solar panels"/>
      <path d="M0 720 C 300 940 700 1020 1200 1010 L1200 1200 L0 1200 Z" fill="var(--red)"/>
      <path d="M0 790 C 300 990 700 1060 1200 1040 L1200 1200 L0 1200 Z" fill="#ffffff"/>
      <g role="img" aria-label="Product photo of a wall-mounted inverter beside a stacked home battery">
        <rect x="700" y="588" width="420" height="520" rx="14" fill="url(#unit)"/>
        <rect x="606" y="768" width="266" height="396" rx="18" fill="#eef0f3"/>
      </g>
    </svg>
    <div class="brand">
      <div class="brand-name"><span class="brand-mark"></span>CORVEL ENERGY</div>
      <div class="brand-tag">ENGINEERING AND ECONOMIC SOLUTIONS</div>
    </div>
    <h1 class="hero-title">Federal Government Battery Subsidy is Coming!</h1>
  </section>

  <h2 class="headline">MAXIMISE<br>YOUR SOLAR SAVINGS</h2>

  <section class="intro">
    <p class="greet">Hi!</p>
    <p class="lead">Great news! With the federal election now decided, the Federal Government’s Home Battery Subsidy Program is officially on the way.</p>
    <p class="body-copy">While the scheme hasn’t formally launched yet, it’s guaranteed—and like the solar rebate before it, the <span class="hl">subsidy reduces each year</span>, so the <span class="hl">earlier you install, the more you’ll save</span>.</p>
    <p class="body-copy">Crucially, the <span class="hl">subsidy is only available once per household</span>, so it makes sense to install a system that fully meets your home’s battery needs right from the start.</p>
  </section>

  <section class="benefits">
    <div class="benefits-bg" role="img" aria-label="Dimmed photo of installed home battery equipment"></div>
    <div class="benefits-panel">
      <div class="benefits-head">Why add a battery to your existing solar system now?</div>
      <ul class="benefit-list">
        <li class="benefit">
          <svg viewBox="0 0 50 54" fill="none" stroke="#fff" stroke-width="2.5"><rect x="13" y="6" width="24" height="44" rx="3"/><rect x="20" y="2" width="10" height="4"/><path d="M27 16 L20 29 H27 L23 41"/></svg>
          <p><b>Store your excess solar energy</b> instead of sending it back to the grid for low feed-in tariffs</p>
        </li>
        <li class="benefit">
          <svg viewBox="0 0 50 54" fill="none" stroke="#fff" stroke-width="2.5"><path d="M26 8 A20 20 0 1 0 44 38 A16 16 0 0 1 26 8 Z"/><circle cx="36" cy="22" r="2"/><circle cx="42" cy="30" r="3"/></svg>
          <p><b>Use your stored solar power at night</b>, when electricity prices are highest (typically 5–8pm)</p>
        </li>
        <li class="benefit">
          <svg viewBox="0 0 50 54" fill="none" stroke="#fff" stroke-width="2.5"><path d="M14 4 H38 V48 H14 Z"/><path d="M20 14 H32 M20 22 H32 M20 30 H28"/><circle cx="14" cy="42" r="7"/></svg>
          <p><b>Slash your power bills</b> and avoid rising time-of-use charges</p>
        </li>
        <li class="benefit">
          <svg viewBox="0 0 50 54" fill="none" stroke="#fff" stroke-width="2.5"><circle cx="25" cy="27" r="20"/><path d="M29 13 L19 29 H27 L21 41"/><path d="M10 42 L40 12"/></svg>
          <p><b>Protect your home</b> from power outages</p>
        </li>
        <li class="benefit">
          <svg viewBox="0 0 50 54" fill="none" stroke="#fff" stroke-width="2.5"><rect x="14" y="6" width="22" height="44" rx="3"/><rect x="20" y="2" width="10" height="4"/><path d="M19 20 H31 M19 28 H31 M19 36 H31"/></svg>
          <p><b>Increase your self-sufficiency</b> and long-term energy security</p>
        </li>
      </ul>
    </div>
  </section>

  <p class="outro">If you’ve already installed solar with us, now is the ideal time to complete your setup with a battery system designed to maximise your return—and take full advantage of this one-off federal subsidy.</p>

  <svg class="cta-arrow" width="36" height="28" viewBox="0 0 36 28"><path d="M0 0 H36 L18 28 Z" fill="var(--navy)"/></svg>
  <a class="cta">Call us today</a>
  <p class="cta-sub">or reply to this email <span class="hl">to secure your spot and beat the rush.</span></p>

  <p class="signoff">Let your solar work smarter for your home,</p>
  <div class="team"><span class="team-mark"></span>The Corvel Energy Team</div>

  <div class="partners">
    <span class="partner p-velto">VELTO</span>
    <span class="partner p-qmp">QMP</span>
    <span class="partner p-brimlite">BRIMLITE</span>
    <span class="partner p-tervo">TervoPWR</span>
  </div>

  <footer class="footer">
    <svg width="1200" height="360" viewBox="0 0 1200 360">
      <path d="M0 130 C 300 40 800 20 1200 170 L1200 360 L0 360 Z" fill="var(--red)"/>
      <path d="M0 162 C 300 76 800 60 1200 230 L1200 360 L0 360 Z" fill="var(--mist)"/>
    </svg>
    <div class="phone-badge">
      <svg width="44" height="44" viewBox="0 0 24 24"><path fill="#fff" d="M6.6 10.8a15.1 15.1 0 0 0 6.6 6.6l2.2-2.2c.3-.3.7-.4 1-.2 1.1.4 2.3.6 3.6.6.6 0 1 .4 1 1V20c0 .6-.4 1-1 1A17 17 0 0 1 3 4c0-.6.4-1 1-1h3.5c.6 0 1 .4 1 1 0 1.3.2 2.5.6 3.6.1.3 0 .7-.2 1z"/></svg>
    </div>
    <div class="phone">07.3555.0148</div>
    <div class="web">www.corvelenergy.com.au</div>
  </footer>

</div>
</body>
</html>
```